Labels for an activated Charcoal Facial Wash, Scrub and Mask

We need a new label design for a new line of Facial products. The product, falls under our Brand Dovelin and is based on Activated Charcoal. Activated Black Charcoal Facial wash (250ml), Activated Black Charcoal Mask (100gms) and Activated Black Charcoal face scrub (100gms). We would like to see designs that are modern, clean and must communicate natural products.

```html
<!DOCTYPE html>
<html lang="en">
<head>
<meta charset="utf-8">
<title>Dovelin Activated Black Charcoal Facial Wash Labels</title>
<link rel="stylesheet" href="https://fonts.googleapis.com/css2?family=Bebas+Neue&family=Kaushan+Script&family=Marcellus&family=Oswald:wght@500&display=swap">
<style>
  :root {
    --stage: #e4e4e4;
    --paper: #ffffff;
    --olive: #4b4f3f;
    --sage: #c8c59f;
    --sage-soft: #ebe9d8;
    --script: #cfcba2;
    --ink: #3a3a33;
  }
  * { box-sizing: border-box; margin: 0; padding: 0; }
  html, body { width: 1200px; height: 900px; overflow: hidden; }
  body {
    background: var(--stage);
    display: flex;
    align-items: center;
    justify-content: center;
    gap: 90px;
  }
  .label {
    position: relative;
    width: 320px;
    height: 760px;
    background: var(--paper);
    overflow: hidden;
    display: flex;
    flex-direction: column;
    align-items: center;
  }
  .leaf-pattern {
    position: absolute;
    inset: 0 0 130px 0;
    background:
      radial-gradient(ellipse at 25% 20%, var(--sage-soft) 0%, transparent 45%),
      radial-gradient(ellipse at 75% 55%, var(--sage-soft) 0%, transparent 45%),
      radial-gradient(ellipse at 30% 85%, var(--sage-soft) 0%, transparent 40%),
      var(--paper);
  }
  .brand {
    position: relative;
    margin-top: 100px;
    width: 150px;
    height: 140px;
    background: var(--paper);
    border: 1px solid var(--sage);
    display: flex;
    align-items: flex-end;
    justify-content: center;
    gap: 7px;
    padding-bottom: 22px;
  }
  .brand-mark {
    width: 7px;
    height: 7px;
    background: var(--sage);
    margin-bottom: 6px;
  }
  .brand-name {
    font-family: "Marcellus", serif;
    font-size: 21px;
    letter-spacing: 4px;
    color: var(--ink);
  }
  .product-panel {
    position: relative;
    margin-top: 70px;
    width: 224px;
    height: 270px;
    background: var(--olive);
    display: flex;
    flex-direction: column;
    align-items: center;
    justify-content: center;
    text-align: center;
  }
  .product-accent {
    font-family: "Kaushan Script", cursive;
    font-size: 30px;
    color: var(--script);
    line-height: 1;
  }
  .product-name {
    font-family: "Bebas Neue", sans-serif;
    color: var(--paper);
    line-height: 0.86;
    margin: 6px 0 4px;
  }
  .product-name .big { display: block; font-size: 92px; letter-spacing: 1px; }
  .product-name .mid { display: block; font-size: 60px; letter-spacing: 1px; }
  .volume-band {
    position: absolute;
    left: 0; right: 0;
    bottom: 150px;
    height: 28px;
    display: flex;
    align-items: center;
    justify-content: center;
    font-family: "Oswald", sans-serif;
    font-weight: 500;
    font-size: 14px;
    letter-spacing: 2px;
  }
  .cap {
    position: absolute;
    left: 0; right: 0; bottom: 0;
    height: 130px;
  }
  .label--dark-cap .volume-band { background: var(--sage); color: var(--paper); }
  .label--dark-cap .cap { background: var(--olive); }
  .label--light-cap .volume-band { background: var(--olive); color: var(--paper); }
  .label--light-cap .cap { background: var(--sage); }
</style>
</head>
<body>
  <section class="label label--dark-cap">
    <div class="leaf-pattern" role="img" aria-label="Fine line leaf pattern in pale sage on white"></div>
    <div class="brand"><span class="brand-mark"></span><span class="brand-name">DOVELIN</span></div>
    <div class="product-panel">
      <span class="product-accent">Activated</span>
      <h1 class="product-name"><span class="big">BLACK</span><span class="mid">CHARCOAL</span></h1>
      <span class="product-accent">Facial wash</span>
    </div>
    <div class="volume-band">250ML</div>
    <div class="cap"></div>
  </section>

  <section class="label label--light-cap">
    <div class="leaf-pattern" role="img" aria-label="Fine line leaf pattern in pale sage on white"></div>
    <div class="brand"><span class="brand-mark"></span><span class="brand-name">DOVELIN</span></div>
    <div class="product-panel">
      <span class="product-accent">Activated</span>
      <h2 class="product-name"><span class="big">BLACK</span><span class="mid">CHARCOAL</span></h2>
      <span class="product-accent">Facial wash</span>
    </div>
    <div class="volume-band">250ML</div>
    <div class="cap"></div>
  </section>
</body>
</html>
```